HomeBridle business card and stationary design

We are looking for a simple yet elegant design for our mortgage company business card and stationary.

The card should include:
Name (Derek Walsh)
Title (CEO)
Phone Number (614-208-3917)
Address (48 Birchfield Court, Suite 314, Marlow, OH 43952)
Email (email@homebridle-example.com)
"NMLS" i.e. (NMLS 61947)
"Company NMLS" (Company NMLS 472815)

See above

```html
<!DOCTYPE html>
<html lang="en">
<head>
<meta charset="utf-8">
<title>HomeBridle Business Card</title>
<link rel="stylesheet" href="https://fonts.googleapis.com/css2?family=Open+Sans:wght@400;600;700&display=swap">
<style>
  :root {
    --backdrop: #d6d6d4;
    --card-dark: #1f2a36;
    --card-dark-edge: #2a3846;
    --card-light: #ffffff;
    --brand-blue: #1fa3e6;
    --ink: #2b3440;
    --rule: #2b3440;
  }
  * { box-sizing: border-box; margin: 0; padding: 0; }
  html, body { width: 1200px; height: 675px; overflow: hidden; }
  body {
    background: var(--backdrop);
    font-family: "Open Sans", Arial, sans-serif;
    position: relative;
  }
  .card {
    position: absolute;
    top: 194px;
    width: 500px;
    height: 286px;
    border-radius: 14px;
    overflow: hidden;
    box-shadow: 0 10px 24px rgba(0,0,0,0.18);
  }
  /* Back of card */
  .card-back { left: 70px; background: var(--card-dark); }
  .card-back .pattern-area {
    position: absolute; inset: 0;
    background: linear-gradient(135deg, var(--card-dark) 0%, var(--card-dark-edge) 50%, var(--card-dark) 100%);
  }
  .card-back .wordmark {
    position: absolute;
    left: 290px; top: 186px;
    font-size: 30px; font-weight: 600;
    color: #ffffff;
    letter-spacing: 0.2px;
  }
  /* Front of card */
  .card-front { left: 630px; background: var(--card-light); }
  .card-front .wordmark {
    position: absolute;
    left: 28px; top: 26px;
    font-size: 38px; font-weight: 600;
    color: var(--brand-blue);
  }
  .card-front .header-rule {
    position: absolute;
    left: 28px; right: 28px; top: 96px;
    height: 1.5px; background: var(--rule);
  }
  .contact-list {
    position: absolute;
    left: 28px; top: 112px;
    list-style: none;
    font-size: 12.5px; color: var(--ink);
    line-height: 24px;
  }
  .contact-list .bullet { margin: 0 6px; }
  .signature {
    position: absolute;
    right: 28px; bottom: 30px;
    text-align: right;
  }
  .signature .name {
    font-size: 19px; font-weight: 700;
    color: var(--brand-blue);
    text-transform: uppercase;
    letter-spacing: 0.3px;
  }
  .signature .title {
    font-size: 11px; font-weight: 700;
    color: var(--ink);
  }
  .signature-rule {
    position: absolute;
    right: 28px; bottom: 22px;
    width: 150px; height: 1.5px;
    background: var(--rule);
  }
</style>
</head>
<body>
  <section class="card card-back">
    <div class="pattern-area" role="img" aria-label="Repeating faint roofline pattern across dark card back"></div>
    <div class="wordmark">HomeBridle</div>
  </section>

  <section class="card card-front">
    <div class="wordmark">HomeBridle</div>
    <div class="header-rule"></div>
    <ul class="contact-list">
      <li>&bull; 48 Birchfield Court, Suite 314, Marlow, OH 43952</li>
      <li>&bull; 614-208-3917<span class="bullet">&bull;</span>email@homebridle-example.com<span class="bullet">&bull;</span>NMLS 61947</li>
    </ul>
    <div class="signature">
      <div class="name">Derek Walsh</div>
      <div class="title">CEO</div>
    </div>
    <div class="signature-rule"></div>
  </section>
</body>
</html>
```